3 Sympathy Cards for Veterinary Hospital

Hi. Brookvale Pet Hospital is a Veterinary Hospital in Australia. We need sympathy cards to send to grieving clients after the loss of their beloved pets.
I have attached the old designs, but we have rebranded and need something to suit our new image.

The cards should have a nice message and appeal to every owner.
They need to match our current branding, but the cards are for the clients, not to advertise us, so not too much branding.
The current cards are attached and they are good because they show a variety of animals so clients might identify with one of them.
I have attached a brown to green gradient that we use on some designs, you don't have to use it, but consider it.
I have attached a logo on background used in some of our new designs, consider using it.
I have attached a font that we use for most new branding.

Target Market(s)

Women 25 to 44

Industry/Entity Type

Veterinary

Font styles to use
Sans Serif
Script

Colors
fac994
cadf82

Requirements
Must have
• IMPORTANT - 3 different designs for the different types of pets.
• 1. Dog.
• 2. Cat.
• 3. Everything else (Rabbits, lizards, ferrets, chickens, birds, mice, rats, snakes)
Nice to have
• Caring and compassionate message.
Should not have
• Too much branding.

```html
<!DOCTYPE html>
<html lang="en">
<head>
<meta charset="utf-8">
<title>Deepest Sympathy Card</title>
<link rel="stylesheet" href="https://fonts.googleapis.com/css2?family=Josefin+Sans:wght@400;700&family=Yesteryear&display=swap">
<style>
  :root {
    --backdrop: #525152;
    --card: #f7d7ae;
    --back-top: #f7d6ae;
    --back-bottom: #d4b593;
    --ink: #6b3a1e;
    --rule: #7a4a2a;
    --frame: #ffffff;
  }
  * { margin: 0; padding: 0; box-sizing: border-box; }
  html, body { width: 1029px; height: 1200px; overflow: hidden; background: var(--backdrop); }
  .card {
    position: absolute; left: 104px; top: 35px; width: 820px; height: 1130px;
  }
  .panel { position: absolute; left: 0; width: 820px; height: 565px; }
  .panel-back {
    top: 0;
    background: linear-gradient(to bottom, var(--back-top) 0%, var(--back-top) 40%, var(--back-bottom) 100%);
  }
  .panel-front { top: 565px; background: var(--card); }

  .back-info {
    position: absolute; left: 0; top: 96px; width: 820px; height: 150px;
    transform: rotate(180deg);
    display: flex; flex-direction: column; align-items: center; justify-content: flex-start;
    color: var(--ink); font-family: "Josefin Sans", sans-serif;
  }
  .brand {
    display: flex; align-items: center; gap: 8px;
    font-weight: 700; font-size: 17px; letter-spacing: 0.5px; text-transform: uppercase;
  }
  .brand-mark { width: 12px; height: 12px; background: var(--ink); }
  .imprint {
    margin-top: 28px; font-size: 9px; line-height: 11px; text-align: center;
  }

  .rule { position: absolute; height: 1px; background: var(--rule); }
  .rule-top { left: 52px; top: 207px; width: 728px; }
  .rule-bottom { left: 58px; top: 401px; width: 718px; }
  .divider { position: absolute; left: 416px; top: 228px; width: 2px; height: 158px; background: var(--rule); }

  .photo-strip {
    position: absolute; top: 250px; height: 114px; width: 340px;
    display: flex; border: 2px solid var(--frame); background: var(--frame); gap: 2px;
  }
  .strip-left { left: 52px; }
  .strip-right { left: 440px; }
  .photo { flex: 1; height: 100%; }
  .photo-spaniel { background: linear-gradient(135deg, #8d8f86, #b0653a 45%, #efe9e2 80%); }
  .photo-dachshund { background: linear-gradient(135deg, #f1ede8, #e6e0d9 50%, #6e3e26 70%, #ece6df); }
  .photo-bulldog { background: linear-gradient(135deg, #f2efea, #e6ddd1 55%, #d9cfc2); }
  .photo-retriever { background: linear-gradient(135deg, #9a8a70, #e4c99d 45%, #c9a877); }

  .message {
    position: absolute; left: 0; top: 410px; width: 820px; text-align: center;
    font-family: "Yesteryear", cursive; font-size: 46px; color: var(--ink);
  }
</style>
</head>
<body>
  <div class="card">
    <section class="panel panel-back">
      <div class="back-info">
        <div class="brand"><span class="brand-mark"></span>Brookvale Pet Hospital</div>
        <p class="imprint">Copyright 2013 Veterinary supplies<br>P.O Box 218, Brookvale 4071 | Ph 1800 4210 36</p>
      </div>
    </section>
    <section class="panel panel-front">
      <div class="rule rule-top"></div>
      <div class="photo-strip strip-left">
        <div class="photo photo-spaniel" role="img" aria-label="Photo of a Cavalier King Charles spaniel puppy holding a pine cone"></div>
        <div class="photo photo-dachshund" role="img" aria-label="Photo of a brown dachshund puppy standing in snow"></div>
      </div>
      <div class="divider"></div>
      <div class="photo-strip strip-right">
        <div class="photo photo-bulldog" role="img" aria-label="Photo of a French bulldog lying on white cushions"></div>
        <div class="photo photo-retriever" role="img" aria-label="Photo of two golden retriever puppies"></div>
      </div>
      <div class="rule rule-bottom"></div>
      <h1 class="message">Deepest Sympathy</h1>
    </section>
  </div>
</body>
</html>
```